PRP Poster

We need a poster for a doctors room to encourage people to enquire about PRP procedure.

It needs to include "for osteoarthritis and sports injuries" and "enhancing the body's natural ability to heal".

A brochure is attached which outlines what PRP (Platelet Rich Plasma) is, in the brochure it is called DVX. DO NOT USE ANY OF THE LOGOS FROM THIS BROCHURE.

Target Market(s)

patients in an orthopaedic surgery waiting room/area
age range from teenagers till 80year olds
male= female ratio

Requirements
Must have
• single poster
eye-catching yet professional
needs to be suitable/appropriate for the waiting area of a surgeons clinic
Nice to have
• prp is a natural therapy (it is essentially the person's own blood being reinjected to a site of injury)
the "natural" aspect of the therapy needs to be emphasised

```html
<!DOCTYPE html>
<html lang="en">
<head>
<meta charset="utf-8">
<title>Platelet Rich Plasma Poster</title>
<link rel="stylesheet" href="https://fonts.googleapis.com/css2?family=Anton&family=PT+Sans+Narrow:wght@700&display=swap">
<style>
  :root {
    --poster-orange: #df4a0e;
    --ink-black: #0c0c0c;
    --text-white: #ffffff;
    --arc-light: rgba(235, 240, 235, 0.75);
    --golf-sky: #e9ece4;
    --golf-trees: #5d6b45;
    --golf-grass: #8fae54;
    --walk-sky: #7fb0e6;
    --walk-haze: #c9dcec;
    --walk-field: #5f8a2e;
  }
  html, body {
    margin: 0;
    padding: 0;
    overflow: hidden;
  }
  .poster {
    position: relative;
    width: 800px;
    height: 1200px;
    background: var(--poster-orange);
    overflow: hidden;
    font-family: "PT Sans Narrow", "Arial Narrow", sans-serif;
    color: var(--text-white);
  }
  .photo-corner {
    position: absolute;
    display: block;
  }
  .photo-corner--top { left: 0; top: 0; }
  .photo-corner--bottom { right: 0; bottom: 0; }
  .indication {
    position: absolute;
    left: 350px;
    top: 146px;
    margin: 0;
    font-weight: 700;
    font-size: 43px;
    line-height: 54px;
    letter-spacing: 0.2px;
  }
  .indication .lead-word { font-size: 31px; }
  .title {
    position: absolute;
    left: 0;
    top: 0;
    display: block;
  }
  .title text {
    font-family: "Anton", "Impact", sans-serif;
    fill: var(--ink-black);
  }
  .natural-claim {
    position: absolute;
    left: 228px;
    top: 786px;
    margin: 0;
    font-weight: 700;
    font-size: 42px;
    line-height: 50px;
  }
  .tagline {
    position: absolute;
    left: 22px;
    top: 915px;
    margin: 0;
    font-weight: 700;
    font-size: 44px;
    line-height: 50px;
  }
</style>
</head>
<body>
<main class="poster">

  <svg class="photo-corner photo-corner--top" width="420" height="320" viewBox="0 0 420 320" role="img" aria-label="Photo of two men playing golf on a green fairway with trees behind">
    <defs>
      <linearGradient id="golf-scene" x1="0" y1="0" x2="0" y2="1">
        <stop offset="0" stop-color="var(--golf-sky)"/>
        <stop offset="0.22" stop-color="var(--golf-trees)"/>
        <stop offset="0.5" stop-color="var(--golf-trees)"/>
        <stop offset="0.62" stop-color="var(--golf-grass)"/>
        <stop offset="1" stop-color="var(--golf-grass)"/>
      </linearGradient>
    </defs>
    <path d="M0 0 H404 C380 150 230 280 0 302 Z" fill="url(#golf-scene)"/>
    <path d="M404 0 C380 150 230 280 0 302 L0 290 C215 268 358 150 382 0 Z" fill="var(--arc-light)"/>
  </svg>

  <p class="indication"><span class="lead-word">FOR</span> ARTHRITIS<br><span class="lead-word">AND</span> SPORTS INJURIES</p>

  <svg class="title" width="800" height="800" viewBox="0 0 800 800" aria-label="Platelet Rich Plasma">
    <text x="173" y="460" font-size="138" textLength="455" lengthAdjust="spacingAndGlyphs">PLATELET</text>
    <text x="173" y="645" font-size="212" textLength="455" lengthAdjust="spacingAndGlyphs">RICH</text>
    <text x="173" y="775" font-size="144" textLength="455" lengthAdjust="spacingAndGlyphs">PLASMA</text>
  </svg>

  <p class="natural-claim">PRP is a Natural Therapy</p>

  <p class="tagline">"Enhancing the Body's<br>Natural Ability to Heal".</p>

  <svg class="photo-corner photo-corner--bottom" width="420" height="300" viewBox="0 0 420 300" role="img" aria-label="Photo of a woman Nordic walking along a path beside green fields under a blue sky">
    <defs>
      <linearGradient id="walk-scene" x1="0" y1="0" x2="0" y2="1">
        <stop offset="0" stop-color="var(--walk-sky)"/>
        <stop offset="0.55" stop-color="var(--walk-haze)"/>
        <stop offset="0.68" stop-color="var(--walk-field)"/>
        <stop offset="1" stop-color="var(--walk-field)"/>
      </linearGradient>
    </defs>
    <path d="M420 12 C255 18 60 120 22 300 H420 Z" fill="url(#walk-scene)"/>
    <path d="M420 0 C250 6 45 110 8 300 H22 C60 120 255 18 420 12 Z" fill="var(--arc-light)"/>
  </svg>

</main>
</body>
</html>
```